Reboot of current Powerpoint Design

We would like to modernise our current powerpoint design which we use for the delivery of class room based training to 5-10 trainees at a time. We have attached our current design but would like a more updated (yet still practical for in-house edits and development).
We would like to be left with a collection of no more than 10-20 master slides for ongoing use in the business. Critically the slides should be focussed on being able to be easily read in a classroom environment, have minimal or no animation (easy to operate by a trainer) and should recognise our customer base which is largely fairly conservative (heavy industry).
In short we are seeking a professional and engaging end result which mirrors our current branding.
Across our entire range of courses we will use the following key structure:
- Title
- Introductory slides
- Overviews
- Modules
- Content
- Discussion
- Conclusion
As part of this update we would like to increase our use of photos (noting that we are not limited to the photos in the current powerpoint so any design should simply use placeholders).
The updated version should incorporate our current branding which is represented in the attached example powerpoint as well as our website (www.brightlaneskills.com).
Thanks
Glen
Updates
Target Market(s)
Safety and compliance in heavy industries (eg. mining, manufacturing, construction, etc.)
Industry/Entity Type
Training
Font styles to use
Other font styles liked:
- Helvetica (or similar to be used on windows machines)
Colors
Designer to choose colors to be used in the design.
Requirements
Must have
- Approximately 20 master slides that can be easily applied across a large number of current power point presentations.
- Strong visual focus with main use in classroom environment (so note that these are used on a projector screen - please take into account (eg. no small fonts).
- We generally use the notes section for any detailed information (trainer benefit) so our focus is on using the slides as triggers for conversations, training structure and headline topics.
- If anything we are focussed on a less is more mentality and are looking for a clean, simple and professional appeal. Note we have no issue in some of the content of the example slides (CPR) moving to the notes section.
- We have also just begun implementing a new brand bi-line which is:
- PlanWell. MoveWell. BuildWell. (Note the Safe. in each word is in BOLD).
- This bi-line needs to be incorporated along with the Brightlane Skills logo in each slide. Please note that we also use the unique A design in the Brightlane Skills logo as a further design feature in our branding documents. As per current powerpoint, we would prefer this to be incorporated as well.
Nice to have
- Functional graphics (easy to edit) and branded icons to ensure we continue to push the Brightlane Skills brand throughout the presentations.
Should not have
- Animation and difficult to edit slides.

```html
<!DOCTYPE html>
<html lang="en">
<head>
<meta charset="utf-8">
<title>Brightlane Skills – Training Slide Masters</title>
<link href="https://fonts.googleapis.com/css2?family=Arimo:wght@400;700&display=swap" rel="stylesheet">
<style>
:root{
  --red:#e0322c;
  --black:#111111;
  --ink:#222222;
  --grey:#5d5d5d;
  --paper:#ffffff;
  --canvas:#ffffff;
  --shadow:rgba(0,0,0,.28);
}
*{box-sizing:border-box;margin:0;padding:0}
html,body{width:1200px;height:2560px;overflow:hidden;background:var(--canvas)}
body{font-family:"Arimo",Helvetica,Arial,sans-serif;color:var(--ink)}
.board{display:grid;grid-template-columns:540px 540px;column-gap:30px;row-gap:46px;padding:25px 0 0 45px}
.slide{position:relative;width:540px;height:304px;background:var(--paper);overflow:hidden;box-shadow:0 2px 6px var(--shadow)}

/* footer */
.footer{position:absolute;left:0;right:0;bottom:0;height:17px;background:var(--black);display:flex;align-items:center;padding:0 0 0 8px;color:#fff}
.footer .brand{font-size:7px;font-weight:700;line-height:1;width:150px;letter-spacing:.3px;white-space:nowrap}
.footer .url{flex:1;text-align:center;font-size:7px;font-weight:700;letter-spacing:1.4px;margin-right:150px;white-space:nowrap}
.footer .pg{position:absolute;right:0;top:0;width:22px;height:17px;background:var(--red);font-size:8px;display:flex;align-items:center;justify-content:center}

/* header */
.mark{position:absolute;left:8px;top:6px;width:46px;height:46px;background:var(--red)}
.stripe{position:absolute;top:14px;width:9px;height:30px;background:var(--black);transform:skewX(-28deg)}
.stripe.s1{left:62px}.stripe.s2{left:76px}
.head{position:absolute;left:88px;right:0;top:14px;height:30px;background:var(--black);color:#fff;display:flex;flex-direction:column;justify-content:center;padding-left:14px}
.head h2{font-size:14px;font-weight:400;white-space:nowrap}
.head small{font-size:8px;font-weight:700;line-height:1}
.head.stack h2{font-size:13px;line-height:1.1}

/* lists */
.bullets{list-style:none}
.bullets li{position:relative;padding-left:16px;font-size:9px;line-height:1.75;color:var(--grey)}
.bullets li::before{content:"";position:absolute;left:2px;top:5px;width:6px;height:6px;background:var(--red)}
.bullets li.lead{color:var(--black);font-weight:700}
.bullets.small li{font-size:7px;line-height:1.5}
.bullets.small li::before{top:3px;width:5px;height:5px}

/* photo placeholders */
.photo{position:absolute}
.ph-site{background:linear-gradient(120deg,#3c3f43,#6b6a5e 55%,#8c7d3f)}
.ph-ice{background:linear-gradient(135deg,#c9c9c7,#8f9091 60%,#6f7072)}
.ph-office{background:linear-gradient(120deg,#4d5156,#777b80)}
.ph-manikin{background:linear-gradient(135deg,#c9a88a,#6f5648)}
.ph-chart{background:linear-gradient(180deg,#2f7d3b,#1f5c2a)}
.ph-danger{background:linear-gradient(135deg,#e9c21c,#2a2a1f)}
.ph-spark{background:radial-gradient(circle at 55% 45%,#f3d8a6,#b26a2e 35%,#1b2333 75%)}
.ph-rescue{background:linear-gradient(90deg,#27313d,#5c6673 60%,#2c3640)}
.ph-phone{background:linear-gradient(135deg,#dfe2e6,#8a9099)}
.ph-person{background:linear-gradient(180deg,#8b8f96,#3b4450)}

/* dark section slides */
.dark .shade{position:absolute;inset:0;background:rgba(20,20,20,.45)}
.block{position:absolute;background:var(--red)}
.band{position:absolute;background:var(--black);color:#fff;display:flex;align-items:center;padding-left:22px;font-size:11px;white-space:nowrap}
.brand-big{position:absolute;color:#fff;font-weight:700;font-size:15px;line-height:1.05;letter-spacing:.5px}

/* frames & callouts */
.frame{position:absolute;border:2px solid var(--black);background:#fff}
.callout{position:absolute;background:var(--red);color:#fff;font-weight:700;font-size:9px;line-height:1.3;padding:8px}
.callout::after{content:"";position:absolute;left:16px;bottom:-9px;border-left:9px solid var(--red);border-bottom:9px solid transparent}
.callout .tick{display:block;width:12px;height:12px;background:var(--black);margin-bottom:6px}
.kicker{display:flex;align-items:center;gap:7px;color:var(--red);font-weight:700;font-size:12px;white-space:nowrap}
.kicker i{display:inline-block;width:13px;height:13px;background:var(--red)}
.contact p{font-size:7.5px;white-space:nowrap}
</style>
</head>
<body>
<main class="board">

  <!-- 1 Title -->
  <section class="slide dark">
    <div class="photo ph-site" style="inset:0" role="img" aria-label="Photo of a site worker in hi-vis vest holding a yellow hard hat"></div>
    <div class="shade"></div>
    <div class="block" style="left:22px;top:40px;width:190px;height:264px"></div>
    <div class="band" style="left:212px;right:0;top:44px;height:30px;font-size:12px">PROVIDE CARDIOPULMONARY RESUSCITATION</div>
    <div style="position:absolute;left:212px;right:0;top:78px;height:1px;background:var(--red)"></div>
    <p style="position:absolute;left:280px;top:86px;color:#fff;font-size:8px;white-space:nowrap">Lorem ipsum dolor sit amet &nbsp;|&nbsp; 01.01.2017 &nbsp;|&nbsp; Lorem ipsum</p>
    <p style="position:absolute;right:22px;top:102px;color:#fff;font-size:11px;font-weight:700">HLTAID001</p>
    <p class="brand-big" style="left:44px;bottom:36px">BRIGHTLANE<br>SKILLS</p>
  </section>

  <!-- 2 Housekeeping (light) -->
  <section class="slide">
    <div class="band" style="left:0;width:370px;top:10px;height:26px;font-size:11px">INTRODUCTION HOUSEKEEPING</div>
    <div style="position:absolute;right:22px;top:6px;width:44px;height:44px;background:var(--red)"></div>
    <ul class="bullets" style="position:absolute;left:118px;top:52px">
      <li class="lead">EMERGENCY EXIT &amp; ASSEMBLY POINT</li><li>Fire extinguishers</li><li>Location of toilets</li><li>Smokers</li><li>Parking</li><li>Any current injuries</li><li>Literacy &amp; numeracy</li><li>Mobile Phones on silence</li><li>Breaks</li>
    </ul>
    <p style="position:absolute;left:12px;bottom:14px;font-size:8px;font-weight:700;color:var(--red)">BRIGHTLANE SKILLS</p>
    <p style="position:absolute;left:220px;bottom:16px;font-size:6px;color:var(--grey)">http://www.brightlaneskills.com</p>
    <p style="position:absolute;right:14px;bottom:16px;font-size:6px;color:var(--grey)">2</p>
    <div style="position:absolute;left:0;right:0;bottom:0;height:6px;background:var(--black)"></div>
  </section>

  <!-- 3 Housekeeping -->
  <section class="slide">
    <div class="mark"></div><div class="stripe s1"></div><div class="stripe s2"></div>
    <header class="head"><h2>INTRODUCTION HOUSEKEEPING</h2></header>
    <ul class="bullets" style="position:absolute;left:104px;top:72px">
      <li class="lead">EMERGENCY EXIT &amp; ASSEMBLY POINT</li><li>Fire extinguishers</li><li>Location of toilets</li><li>Smokers</li><li>Parking</li><li>Any current injuries</li><li>Literacy &amp; numeracy</li><li>Mobile Phones on silence</li><li>Breaks</li>
    </ul>
    <footer class="footer"><span class="brand">BRIGHTLANE SKILLS</span><span class="url">http://www.brightlaneskills.com</span><span class="pg">3</span></footer>
  </section>

  <!-- 4 Section: exit -->
  <section class="slide dark">
    <div class="photo ph-site" style="inset:0" role="img" aria-label="Photo of a site worker holding a yellow hard hat"></div>
    <div class="shade"></div>
    <div class="block" style="left:150px;top:130px;width:160px;height:174px"></div>
    <div class="band" style="left:160px;right:22px;top:118px;height:30px">EMERGENCY EXIT &amp; ASSEMBLY POINT</div>
    <p class="brand-big" style="right:18px;bottom:22px">BRIGHTLANE<br>SKILLS</p>
  </section>

  <!-- 5 Course objectives -->
  <section class="slide">
    <div class="mark"></div><div class="stripe s1"></div><div class="stripe s2"></div>
    <header class="head stack"><small>Introduction</small><h2>Course Objectives</h2></header>
    <h3 style="position:absolute;left:42px;top:110px;font-size:14px;color:var(--black)">Unit of Competency HLTAID001</h3>
    <ul class="bullets" style="position:absolute;left:56px;top:134px">
      <li>Respond to an emergency situation</li><li>Perform CPR Procedures</li><li>Communicate Details of the Incident</li>
    </ul>
    <div style="position:absolute;left:392px;top:96px;width:80px;height:80px;border-radius:50%;background:#2c4fb5" role="img" aria-label="Partner council badge"></div>
    <footer class="footer"><span class="brand">BRIGHTLANE SKILLS</span><span class="url">http://www.brightlaneskills.com</span><span class="pg">5</span></footer>
  </section>

  <!-- 6 Icebreaker -->
  <section class="slide dark">
    <div class="photo ph-ice" style="inset:0" role="img" aria-label="Photo of cracked ice surface"></div>
    <div class="block" style="left:0;top:0;width:220px;height:304px"></div>
    <div class="band" style="left:200px;right:0;top:104px;height:30px;justify-content:flex-end;padding-right:30px">ICEBREAKER</div>
    <p class="brand-big" style="right:18px;bottom:30px">BRIGHTLANE<br>SKILLS</p>
    <footer class="footer"><span class="brand">BRIGHTLANE SKILLS</span><span class="url">http://www.brightlaneskills.com</span><span class="pg">6</span></footer>
  </section>

  <!-- 7 Respond: hazards -->
  <section class="slide">
    <div class="mark"></div><div class="stripe s1"></div><div class="stripe s2"></div>
    <header class="head"><h2>Respond to an emergency situation</h2></header>
    <div class="photo ph-manikin" style="left:42px;top:76px;width:180px;height:182px" role="img" aria-label="Photo of hands performing chest compressions on a CPR manikin"></div>
    <div class="frame" style="left:228px;top:76px;width:290px;height:182px"></div>
    <div class="photo ph-chart" style="left:238px;top:88px;width:104px;height:158px" role="img" aria-label="Basic life support flowchart poster"></div>
    <div class="callout" style="left:352px;top:110px;width:116px;height:96px"><span class="tick"></span>Identify, assess and minimise immediate hazards!</div>
    <footer class="footer"><span class="brand">BRIGHTLANE SKILLS</span><span class="url">http://www.brightlaneskills.com</span><span class="pg">7</span></footer>
  </section>

  <!-- 8 Respond: danger -->
  <section class="slide">
    <div class="mark"></div><div class="stripe s1"></div><div class="stripe s2"></div>
    <header class="head"><h2>Respond to an emergency situation</h2></header>
    <div class="photo ph-danger" style="left:42px;top:76px;width:180px;height:182px" role="img" aria-label="Photo of yellow and black danger warning tape"></div>
    <div class="frame" style="left:228px;top:76px;width:286px;height:182px"></div>
    <div style="position:absolute;left:244px;top:88px">
      <p class="kicker"><i></i>The rescuer must:</p>
      <p style="font-size:11px;color:var(--grey);padding-left:20px;white-space:nowrap">Assess the situation quickly for?</p>
    </div>
    <ul class="bullets" style="position:absolute;left:252px;top:140px"><li>Rescuer</li><li>Bystanders</li><li>Casualty</li></ul>
    <div class="callout" style="left:406px;top:150px;width:84px;height:70px"><span class="tick"></span>Priorities in an Emergency!!</div>
    <footer class="footer"><span class="brand">BRIGHTLANE SKILLS</span><span class="url">http://www.brightlaneskills.com</span><span class="pg">8</span></footer>
  </section>

  <!-- 9 Respond: electric shock -->
  <section class="slide">
    <div class="mark"></div><div class="stripe s1"></div><div class="stripe s2"></div>
    <header class="head"><h2>Respond to an emergency situation</h2></header>
    <div class="photo ph-spark" style="left:42px;top:76px;width:180px;height:182px" role="img" aria-label="Photo of sparks from an electrical cable"></div>
    <div class="frame" style="left:228px;top:76px;width:286px;height:182px"></div>
    <p class="kicker" style="position:absolute;left:244px;top:100px"><i></i>Electric Shock</p>
    <ul class="bullets" style="position:absolute;left:252px;top:134px"><li>Assess the DANGER</li><li>Isolate the casualty</li><li>Assess the casualty</li></ul>
    <div class="callout" style="left:406px;top:140px;width:84px;height:70px"><span class="tick"></span>Priorities in an Emergency!!</div>
    <footer class="footer"><span class="brand">BRIGHTLANE SKILLS</span><span class="url">http://www.brightlaneskills.com</span><span class="pg">9</span></footer>
  </section>

  <!-- 10 Moving a victim -->
  <section class="slide">
    <div class="mark"></div><div class="stripe s1"></div><div class="stripe s2"></div>
    <header class="head"><h2>Respond to an emergency situation</h2></header>
    <h3 style="position:absolute;left:42px;top:108px;font-size:14px;color:var(--black)">Moving an Injured Victim</h3>
    <ul class="bullets" style="position:absolute;left:52px;top:134px;width:320px">
      <li>A rescuer should move a collapsed or injured victim:</li>
      <li>Where extreme weather conditions deem it essential</li>
      <li>To make possible the care of airway, breathing &amp; compression</li>
      <li>To make possible the control of severe bleeding</li>
    </ul>
    <div class="callout" style="left:386px;top:118px;width:124px;height:100px"><span class="tick"></span>THE AIRWAY TAKES PRECEDENCE OVER ANY FRACTURE</div>
    <footer class="footer"><span class="brand">BRIGHTLANE SKILLS</span><span class="url">http://www.brightlaneskills.com</span><span class="pg">10</span></footer>
  </section>

  <!-- 11 COWS -->
  <section class="slide">
    <div class="mark"></div><div class="stripe s1"></div><div class="stripe s2"></div>
    <header class="head"><h2>Respond to an emergency situation</h2></header>
    <h3 style="position:absolute;left:56px;top:84px;font-size:13px;color:var(--black)">RESPONSIVE</h3>
    <ul class="bullets" style="position:absolute;left:160px;top:78px">
      <li style="color:var(--red)">C – CAN YOU HEAR ME</li><li style="color:var(--red)">O – OPEN YOUR EYES</li><li style="color:var(--red)">W – WHAT IS YOUR NAME</li><li style="color:var(--red)">S – SQUEEZE MY HANDS</li>
    </ul>
    <p class="kicker" style="position:absolute;right:24px;top:118px;font-size:15px">Electric Shock<i></i></p>
    <div class="photo ph-rescue" style="left:60px;top:148px;width:460px;height:124px" role="img" aria-label="Photo of a rescuer checking a casualty lying on the ground"></div>
    <footer class="footer"><span class="brand">BRIGHTLANE SKILLS</span><span class="url">http://www.brightlaneskills.com</span><span class="pg">11</span></footer>
  </section>

  <!-- 12 Communicate -->
  <section class="slide">
    <div class="mark"></div><div class="stripe s1"></div><div class="stripe s2"></div>
    <header class="head"><h2>Communicate details of the incident</h2></header>
    <div class="photo ph-phone" style="left:24px;top:64px;width:124px;height:66px" role="img" aria-label="Photo of a desk telephone"></div>
    <div class="photo ph-phone" style="left:24px;top:134px;width:124px;height:66px" role="img" aria-label="Photo of a mobile phone"></div>
    <div class="photo ph-phone" style="left:24px;top:204px;width:124px;height:66px" role="img" aria-label="Photo of a two-way radio"></div>
    <p style="position:absolute;left:208px;top:70px;width:310px;font-size:7.5px;line-height:1.35;color:var(--grey)">When you initiate the emergency call you must state that “this is an emergency” or “emergency, emergency, emergency” and be ready to give the following information:</p>
    <h3 style="position:absolute;left:208px;top:102px;font-size:15px;color:var(--red);white-space:nowrap">Initiating Emergency Response</h3>
    <div class="frame" style="left:208px;top:124px;width:304px;height:140px;border-color:var(--red);border-width:1.5px"></div>
    <ul class="bullets small" style="position:absolute;left:214px;top:130px;width:150px">
      <li>Your name</li><li>Your location</li><li>The number of the telephone that you are ringing from</li><li>Exact location of the incident / emergency</li><li>Type of incident</li><li>Number of persons injured</li>
    </ul>
    <ul class="bullets small" style="position:absolute;left:370px;top:130px;width:140px">
      <li>What assistance is required</li><li>What hazards exist</li>
    </ul>
    <div class="callout" style="left:376px;top:174px;width:128px;height:58px;font-size:8.5px">DO NOT HANG UP UNTIL YOU ARE TOLD TO DO SO!!!</div>
    <footer class="footer"><span class="brand">BRIGHTLANE SKILLS</span><span class="url">http://www.brightlaneskills.com</span><span class="pg">12</span></footer>
  </section>

  <!-- 13 Summary -->
  <section class="slide dark">
    <div class="photo ph-office" style="inset:0" role="img" aria-label="Photo of people in a business meeting"></div>
    <div class="shade"></div>
    <div class="block" style="left:96px;top:0;width:180px;height:304px"></div>
    <div class="band" style="left:180px;width:320px;top:70px;height:28px;transform:skewX(-18deg)"><span style="transform:skewX(18deg)">SUMMARY</span></div>
    <div class="band" style="left:180px;width:320px;top:106px;height:28px;transform:skewX(-18deg)"><span style="transform:skewX(18deg)">What have we learnt from this course</span></div>
    <div class="band" style="left:180px;width:320px;top:142px;height:28px;transform:skewX(-18deg)"><span style="transform:skewX(18deg)">QUESTIONS?</span></div>
    <p class="brand-big" style="left:138px;bottom:30px">BRIGHTLANE<br>SKILLS</p>
    <footer class="footer"><span class="brand">BRIGHTLANE SKILLS</span><span class="url">http://www.brightlaneskills.com</span><span class="pg">13</span></footer>
  </section>

  <!-- 14 Contact -->
  <section class="slide dark">
    <div class="photo ph-office" style="inset:0" role="img" aria-label="Background photo of an office"></div>
    <div class="shade"></div>
    <div class="block" style="left:0;top:0;width:190px;height:304px"></div>
    <div class="photo ph-person" style="left:376px;top:28px;width:140px;height:276px" role="img" aria-label="Photo of a trainer in a suit with arms folded"></div>
    <div class="contact" style="position:absolute;left:240px;top:40px;color:#fff;line-height:1.35">
      <p style="font-size:13px">Lorem ipsum dolor</p>
      <p style="font-size:8px;font-weight:700">+61 3 5550 0142</p>
      <p>hello@brightlaneskills.com</p>
      <p>1234 Lorem ipsum dolor</p>
      <p>Donec quam felis</p>
      <p>Nullam dictum felis eu</p>
    </div>
    <p class="brand-big" style="right:18px;bottom:22px">BRIGHTLANE<br>SKILLS</p>
  </section>

</main>
</body>
</html>
```